Campaign Flyer for a local election

Black and white election flyer

See information below to be included:

Re-elect Morton
Experienced Glenmoor Board Member
Experienced NYC Principal
Experienced leader

One Year Board Accomplishments:
-Installed New Park Lights (Bollards)
-Red Brick Road Repair Project
-Established Closer Ties with Our local precinct to frequently monitor the community with directed security patrols. Requested an increased police presence.
-Met with the 82nd Precinct Officials & Assemblywoman, Linda Marwick to discuss our security issues
- Focused on maintenance of streetlights to make brighter streets
-Negotiated Contract & Hired Our New Landscaper, Hollowfield Landscapers
-Major Homeowner Shrub Replacement Project
- Addressing Standing Water in our Park (Installed French Drain)
- Replaced and upgraded all 5 outdoor circuit breaker panels
-Write monthly community newsletters
-Sewer cleaning project (had all community catch basins cleaned)
-Carefully overseeing our new school project. Coordinating with the sponsor and the school directors
-Delivered a very healthy budget to the community
-Works closely with our committees
-Events: Zoo event, Petting Zoo, Outdoor Movie Night, Egg Hunt

It is my intent to seek re-election.
(Photo) Morton Velasquez
-Dedicated to improving our community
-Hard-working…He gets thing done!
-Trustworthy

. .

Please note, I am submitting new information under accomplishments. The list of accomplishments should be in the same sequence, starting with: Met with the 82nd Precinct....
Please carefully review.
----------------------------------------------------------------------------------------------------------------------------------------------------------------

Re-elect Morton
Experienced NYC Principal
Experienced leader

Last Year’s Board Accomplishments:

-Met with the 82nd Precinct Officials & Assemblywoman, Linda Marwick, to discuss our security issues. Requested increased police presence.
-Established a strong partnership with the 82nd precinct to frequently monitor the community with directed security patrols.
-Replaced all new park lights (Bollards) to make the park brighter
- Focused on maintenance of streetlights to make streets brighter
-‘Fixing Our Streets Project’ (Repaired all cracked/missing red bricks)
-Homeowner Shrub Replacement Project (Replaced hundreds of bushes)
- I write the monthly community newsletter
-Carefully overseeing our new school project. Coordinating with the sponsor and the school director
-Monitoring C of O’s and homeowners Insurance

(Photo) Morton Velasquez
-Hard-working! I get things done!
-Trustworthy

. .

Re-elect Morton
Experienced NYC Principal
Experienced leader

(Photo) Morton Velasquez
-Trustworthy

. .

Target Market(s)

A Community electing a Board Member

Industry/Entity Type

residential election

Requirements
Must have
• all black, white and grey print. Flyers will not be printed in color
Nice to have
• See the information in the attachment below containing all my accomplishments
Should not have
• color

```html
<!DOCTYPE html>
<html lang="en">
<head>
<meta charset="utf-8">
<title>Re-elect Morton Velasquez – Campaign Flyer</title>
<link href="https://fonts.googleapis.com/css2?family=League+Gothic&family=Roboto+Condensed:ital,wght@0,400;0,700;1,700&display=swap" rel="stylesheet">
<style>
:root{
  --ink:#000;
  --paper:#fff;
  --page:#ffffff;
  --grey-light:#d0d0d0;
  --grey-mid:#8a8a8a;
  --grey-dark:#555;
  --rule:#bdbdbd;
}
*{margin:0;padding:0;box-sizing:border-box}
html,body{width:1200px;height:1095px;overflow:hidden;background:var(--page)}
.flyer{
  position:absolute;left:297px;top:145px;width:1004px;height:1418px;
  transform:scale(0.6026);transform-origin:0 0;
  background:var(--paper);overflow:hidden;
  font-family:"Roboto Condensed",sans-serif;color:var(--ink);
  box-shadow:0 4px 14px rgba(0,0,0,.25);
}
.flyer-art{position:absolute;inset:0}
.headline{
  position:absolute;left:52px;top:38px;
  font-family:"League Gothic",sans-serif;font-size:198px;line-height:1;
  color:var(--paper);letter-spacing:1px;white-space:nowrap;
}
.headline .first-name{color:var(--grey-light)}
.credentials{position:absolute;left:57px;top:212px;list-style:none}
.credentials li{
  display:flex;align-items:center;gap:14px;height:49.5px;
  font-size:40px;color:var(--paper);
}
.credentials svg{width:32px;height:32px}
.section-label{
  position:absolute;left:0;top:556px;width:420px;text-align:center;
  font-weight:700;font-size:36px;line-height:38px;color:var(--paper);
}
.accomplishments{
  position:absolute;left:468px;top:402px;width:470px;list-style:none;
}
.accomplishments li{
  position:relative;padding:4px 0 5px 18px;
  font-size:16.5px;line-height:20px;border-bottom:1px solid var(--rule);
}
.accomplishments li:last-child{border-bottom:none}
.accomplishments li::before{
  content:"";position:absolute;left:0;top:9px;width:10px;height:10px;border-radius:50%;
  background:var(--ink);box-shadow:inset 0 0 0 2px var(--ink),inset 0 0 0 3px var(--paper);
}
.quote{
  position:absolute;right:46px;top:1106px;
  font-weight:700;font-style:italic;font-size:45px;color:var(--paper);white-space:nowrap;
}
.candidate-name{
  position:absolute;left:52px;top:1150px;width:910px;
  font-family:"League Gothic",sans-serif;font-size:172px;line-height:1;letter-spacing:1px;white-space:nowrap;
  background:linear-gradient(#ffffff 25%,#9a9a9a 100%);
  -webkit-background-clip:text;background-clip:text;color:transparent;
}
.qualities{list-style:none;position:absolute;top:1314px;left:0;width:100%}
.qualities li{
  position:absolute;display:flex;align-items:center;gap:20px;
  font-weight:700;font-size:32px;color:#111;white-space:nowrap;
}
.qualities svg{width:18px;height:18px}
.qualities li:nth-child(1){left:245px;top:0}
.qualities li:nth-child(2){left:280px;top:33px}
.qualities li:nth-child(3){left:396px;top:65px}
</style>
</head>
<body>
<div class="flyer">
  <svg class="flyer-art" viewBox="0 0 1004 1418" width="1004" height="1418">
    <defs>
      <linearGradient id="sky" x1="0" y1="0" x2="0" y2="1">
        <stop offset="0" stop-color="#fafafa"/>
        <stop offset=".4" stop-color="#e4e4e4"/>
        <stop offset=".55" stop-color="#9c9c9c"/>
        <stop offset="1" stop-color="#7a7a7a"/>
      </linearGradient>
      <linearGradient id="footer" x1="0" y1="0" x2="1" y2="0">
        <stop offset="0" stop-color="#b5b5b5"/>
        <stop offset=".5" stop-color="#ececec"/>
        <stop offset="1" stop-color="#b5b5b5"/>
      </linearGradient>
      <linearGradient id="swoosh" x1="0" y1="0" x2="1" y2="0">
        <stop offset="0" stop-color="#e6e6e6"/>
        <stop offset="1" stop-color="#7d7d7d"/>
      </linearGradient>
      <radialGradient id="badge" cx=".4" cy=".35" r=".7">
        <stop offset="0" stop-color="#f2f2f2"/>
        <stop offset="1" stop-color="#a8a8a8"/>
      </radialGradient>
      <linearGradient id="portrait" x1="0" y1="0" x2="0" y2="1">
        <stop offset="0" stop-color="#ececec"/>
        <stop offset="1" stop-color="#8c8c8c"/>
      </linearGradient>
      <path id="badge-ring" d="M859,308 m-62,0 a62,62 0 1,1 124,0 a62,62 0 1,1 -124,0"/>
    </defs>

    <rect class="beach-photo" x="0" y="330" width="1004" height="650" fill="url(#sky)" role="img" aria-label="Photo of a beach with dune fencing and sea grass"/>
    <rect class="base-band" x="0" y="972" width="1004" height="336" fill="var(--ink)"/>
    <rect class="footer-band" x="0" y="1308" width="1004" height="110" fill="url(#footer)"/>

    <path class="header-swoosh" d="M0,350 C70,380 160,420 270,445 C360,462 450,440 570,378 C700,312 850,285 1004,322 V300 C850,262 700,288 560,356 C430,420 330,440 260,420 C150,400 60,370 0,345 Z" fill="url(#swoosh)"/>
    <path class="header-band" d="M0,0 H1004 V300 C850,262 700,288 560,356 C430,420 330,440 260,420 C150,400 60,370 0,345 Z" fill="var(--ink)"/>

    <polygon class="label-arrow" points="0,537 408,537 440,598 408,660 0,660" fill="var(--ink)"/>

    <rect class="panel-frame" x="507" y="367" width="468" height="640" fill="var(--grey-mid)"/>
    <polygon class="panel" points="437,380 962,380 962,1030 697,1092 437,1030" fill="var(--paper)"/>
    <path class="panel-bracket" d="M470,390 H453 V1012 H470" fill="none" stroke="var(--ink)" stroke-width="3"/>

    <g class="vote-badge">
      <circle cx="859" cy="308" r="86" fill="url(#badge)" stroke="#6a6a6a" stroke-width="1"/>
      <text font-family="Roboto Condensed, sans-serif" font-weight="700" font-size="21" letter-spacing="1.5" fill="var(--ink)">
        <textPath href="#badge-ring" startOffset="0">VOTE · VOTE · VOTE · VOTE ·</textPath>
      </text>
      <path d="M834,310 L852,328 L884,288" fill="none" stroke="var(--ink)" stroke-width="9" stroke-linecap="round" stroke-linejoin="round"/>
    </g>

    <path class="portrait-frame" d="M73,837 H293 V1095 A60,60 0 0 1 233,1155 H73 Z" fill="none" stroke="var(--paper)" stroke-width="2"/>
    <rect class="portrait" x="88" y="850" width="190" height="292" fill="url(#portrait)" role="img" aria-label="Portrait photo of Morton Velasquez"/>
  </svg>

  <h1 class="headline">Re-elect <span class="first-name">Morton</span></h1>

  <ul class="credentials">
    <li><svg viewBox="0 0 32 32"><path d="M4,17 L12,25 L28,7" fill="none" stroke="#fff" stroke-width="4"/></svg>Experienced Glenmoor Board Member</li>
    <li><svg viewBox="0 0 32 32"><path d="M4,17 L12,25 L28,7" fill="none" stroke="#fff" stroke-width="4"/></svg>Experienced NYC Principal</li>
    <li><svg viewBox="0 0 32 32"><path d="M4,17 L12,25 L28,7" fill="none" stroke="#fff" stroke-width="4"/></svg>Experienced leader</li>
  </ul>

  <h2 class="section-label">Last Year's<br>Board Accomplishments:</h2>

  <ul class="accomplishments">
    <li>Met with the 82nd Precinct Officials &amp; Assemblywoman, Linda Marwick, to discuss our security issues. Requested increased police presence.</li>
    <li>Established a strong partnership with the 82nd precinct to frequently monitor the community with directed security patrols.</li>
    <li>Replaced all new park lights (Bollards) to make the park brighter</li>
    <li>Focused on maintenance of streetlights to make streets brighter</li>
    <li>‘Fixing Our Streets Project’ (Repaired all cracked/missing red bricks)</li>
    <li>Negotiated Contract &amp; Hired Our New Landscaper, Hollowfield Landscapers</li>
    <li>Homeowner Shrub Replacement Project (Replaced hundreds of bushes)</li>
    <li>Addressing Standing Water in our Park (Installed French Drain)</li>
    <li>Replaced and upgraded all 5 outdoor circuit breaker panels</li>
    <li>I write the monthly community newsletter</li>
    <li>Sewer cleaning project (had all community catch basins cleaned)</li>
    <li>Carefully overseeing our new school project. Coordinating with the sponsor and the school director</li>
    <li>Delivered a very healthy budget to the community</li>
    <li>Works closely with our committees</li>
    <li>Monitoring C of O’s and homeowners Insurance</li>
    <li>Events: Zoo event, Petting Zoo, Outdoor Movie Night, Egg Hunt</li>
  </ul>

  <p class="quote">"It is my intent to seek re-election"</p>
  <p class="candidate-name">Morton Velasquez</p>

  <ul class="qualities">
    <li><svg viewBox="0 0 18 18"><path d="M2,10 L7,15 L16,4" fill="none" stroke="#8a8a8a" stroke-width="2"/></svg>Dedicated to improving our community</li>
    <li><svg viewBox="0 0 18 18"><path d="M2,10 L7,15 L16,4" fill="none" stroke="#8a8a8a" stroke-width="2"/></svg>Hard-working!&nbsp; I get things done!</li>
    <li><svg viewBox="0 0 18 18"><path d="M2,10 L7,15 L16,4" fill="none" stroke="#8a8a8a" stroke-width="2"/></svg>Trustworthy</li>
  </ul>
</div>
</body>
</html>
```